Tidal Ledger

Please see attached Word document for requirements. I want the website to be one page.

Coding

Coded - Design and coding required

Number of Pages Required

1 page

Colors
0054AA
0677BA
7BADD7
CADEEF
E8F1F8

```html
<!DOCTYPE html>
<html lang="en">
<head>
<meta charset="utf-8">
<title>Tidal Ledger — Workforce Scheduling</title>
<link href="https://fonts.googleapis.com/css2?family=Barlow+Condensed:wght@500;600&family=Montserrat:wght@300;400;500;600;700&display=swap" rel="stylesheet">
<style>
:root{
  --primary:#0054AA;
  --secondary:#0677BA;
  --sky:#7BADD7;
  --pale:#CADEEF;
  --mist:#E8F1F8;
  --ink:#1c2433;
  --muted:#6b7585;
  --line:#dfe6ee;
  --footer:#0d1a33;
  --white:#ffffff;
}
*{box-sizing:border-box;margin:0;padding:0}
html,body{width:1200px;height:5305px;overflow:hidden}
body{font-family:"Montserrat",sans-serif;color:var(--ink);background:var(--white);position:relative}
section,header,footer{position:absolute;left:0;width:1200px}
.abs{position:absolute}
.cond{font-family:"Barlow Condensed",sans-serif}
.center{text-align:center;left:0;width:1200px}

/* header */
.site-header{top:0;height:80px}
.brand{left:106px;top:24px;display:flex;align-items:center;gap:8px;font-size:27px;font-weight:600;color:#5b6a80}
.brand-dot{width:14px;height:14px;border-radius:50%;background:var(--secondary)}
.nav-link{top:31px;font-size:12px;color:#3b4556;white-space:nowrap}
.btn{display:inline-flex;align-items:center;justify-content:center;gap:8px;border-radius:40px;font-weight:600;font-size:12px;white-space:nowrap}
.btn-solid{background:var(--primary);color:var(--white)}
.btn-outline{border:1.5px solid var(--primary);color:var(--primary);background:var(--white)}
.header-cta{left:967px;top:21px;width:126px;height:36px}

/* hero */
.hero{top:80px;height:520px}
.hero-title{left:107px;top:98px;font-size:46px;font-weight:600;line-height:56px;color:#1d2a3d}
.hero-curve{left:262px;top:204px}
.hero-text{left:107px;top:232px;width:360px;font-size:13px;line-height:22px;color:#3d4656}
.hero-btn1{left:106px;top:325px;width:162px;height:42px}
.hero-btn2{left:281px;top:325px;width:162px;height:42px}
.hero-art{left:590px;top:40px;width:545px;height:410px;border-radius:30px;background:radial-gradient(circle at 55% 40%,#d7e6f6 0%,#eef4fb 55%,#ffffff 80%)}

/* trust */
.trust{top:600px;height:203px}
.trust-label{top:30px;font-size:13px;letter-spacing:2px;font-weight:500;color:#2e3645}
.trust-row{left:140px;top:82px;width:920px;display:flex;justify-content:space-between;align-items:center;font-size:28px;font-weight:700;color:#4d5563}
.trust-row span{display:flex;align-items:center;gap:8px}
.trust-sq{width:22px;height:22px;background:#8a919c;border-radius:4px}

/* why */
.why{top:803px;height:473px;background:var(--mist)}
.eyebrow{font-size:12px;font-weight:600;letter-spacing:1.5px;color:var(--primary)}
.sec-title{font-size:38px;font-weight:500;color:#1d2a3d}
.why-card{top:179px;width:284px;height:210px;background:var(--white);border-radius:6px;box-shadow:0 8px 22px rgba(0,60,120,.10);padding:24px 24px}
.why-card h3{margin-top:22px;font-size:16px;font-weight:600;color:#1f2a3a}
.why-card p{margin-top:14px;font-size:11.5px;line-height:18px;color:var(--muted)}

/* features */
.features{top:1276px;height:813px}
.hex-wrap{width:263px;height:298px;filter:drop-shadow(0 8px 16px rgba(0,60,120,.12))}
.hex{width:100%;height:100%;clip-path:polygon(50% 0,100% 25%,100% 75%,50% 100%,0 75%,0 25%);background:var(--white);display:flex;flex-direction:column;align-items:center;justify-content:center;text-align:center;padding:0 32px}
.hex h3{margin-top:14px;font-size:16px;font-weight:600;color:#1f2a3a}
.hex p{margin-top:10px;font-size:11.5px;line-height:18px;color:var(--muted)}
.hex.active{background:var(--primary)}
.hex.active h3,.hex.active p{color:var(--white)}

/* industries */
.industries{top:2089px;height:381px;background:var(--mist)}
.ind{top:180px;width:140px;margin-left:-70px;display:flex;flex-direction:column;align-items:center;gap:22px;font-size:14px;color:#2c3545}
.ind-circle{width:82px;height:82px;border-radius:50%;background:var(--white);border:4px solid #dce7f3;display:flex;align-items:center;justify-content:center}
.ind-circle.active{background:var(--primary);border-color:#b9d0ea}

/* testimonials */
.testimonials{top:2470px;height:586px}
.pill{display:inline-block;border:1px solid var(--primary);border-radius:20px;padding:6px 16px;font-size:11px;color:var(--primary);background:var(--white)}
.sec-title-alt{font-size:37px;font-weight:400;color:#1d2a3d}
.sec-title-alt b{font-weight:700}
.t-card{top:201px;width:288px;height:295px;background:var(--white);border-radius:6px;box-shadow:0 6px 22px rgba(0,40,90,.10);padding:18px 22px}
.t-avatar{position:absolute;left:14px;top:14px;width:82px;height:82px;border-radius:50%;background:linear-gradient(135deg,#c9a58c,#7c8ea3)}
.t-name{position:absolute;left:107px;top:29px;font-size:14px;font-weight:500;white-space:nowrap}
.t-stars{position:absolute;left:107px;top:50px;color:#f2b01e;font-size:13px;letter-spacing:2px}
.t-quote{position:absolute;right:14px;top:14px;font-family:"Barlow Condensed",sans-serif;font-size:38px;font-weight:600;color:var(--secondary);line-height:1}
.t-text{position:absolute;left:22px;top:110px;width:245px;font-size:11px;line-height:21px;color:#3d4656}
.arrow{width:38px;height:38px;border-radius:50%;display:flex;align-items:center;justify-content:center;top:330px}

/* pricing */
.pricing{top:3056px;height:844px;background:var(--mist)}
.p-card{top:231px;width:292px;height:531px;background:var(--white);border-radius:12px;box-shadow:0 8px 22px rgba(0,50,110,.10);padding:26px 26px}
.p-card.featured{background:var(--primary);color:var(--white)}
.p-card h3{margin-top:18px;font-size:19px;font-weight:600}
.p-sub{font-size:9.5px;color:var(--muted);margin-top:6px}
.featured .p-sub{color:#b9d3ee}
.p-price{margin-top:18px;font-size:38px;font-weight:600;color:var(--primary);display:flex;align-items:baseline;gap:8px}
.p-price small{font-size:10px;font-weight:400;color:var(--muted)}
.featured .p-price,.featured .p-price small{color:var(--white)}
.p-choose{margin-top:20px;font-size:25px;font-weight:600;color:var(--primary)}
.p-rule{height:1px;background:var(--line);margin:16px 0 12px}
.featured .p-rule{background:rgba(255,255,255,.25)}
.p-get{font-size:11px;font-weight:600}
.p-list{list-style:none;margin-top:10px}
.p-list li{display:flex;align-items:center;gap:9px;font-size:11px;height:32px}
.tick{width:12px;height:12px;border-radius:50%;background:var(--primary);flex:none;display:flex;align-items:center;justify-content:center}
.featured .tick{background:var(--white)}
.p-btn{position:absolute;left:28px;bottom:32px;width:236px;height:38px;border-radius:3px;background:var(--primary);color:var(--white);font-size:11px;font-weight:700;display:flex;align-items:center;justify-content:center}
.featured .p-btn{background:var(--white);color:var(--primary)}
.badge{position:absolute;right:16px;top:24px;background:var(--white);color:var(--primary);font-size:8px;font-weight:700;border-radius:10px;padding:4px 8px}

/* contact */
.contact{top:3900px;height:634px}
.contact-sub{top:190px;font-size:11px;line-height:16px;color:#3b4556}
.field{height:50px;border:1.5px solid var(--line);border-radius:3px;display:flex;align-items:center;gap:16px;padding:0 14px;font-size:11px;color:var(--muted)}
.contact-btn{left:292px;top:500px;width:616px;height:50px;border-radius:3px;background:linear-gradient(90deg,var(--primary),#0a9ad8);color:var(--white);font-size:12px;font-weight:700;display:flex;align-items:center;justify-content:center}

/* cta */
.cta{top:4534px;left:142px;width:916px;height:331px;border-radius:30px;background:linear-gradient(100deg,#0a57ad,#0a66bd 60%,#0b5fb3);color:var(--white);text-align:center}
.cta h2{margin-top:78px;font-size:42px;font-weight:300;line-height:52px}
.cta h2 b{font-weight:600}
.cta p{margin-top:12px;font-size:11px}
.cta-btns{margin-top:22px;display:flex;justify-content:center;gap:16px}
.cta-btns span{width:154px;height:44px;border-radius:4px;display:flex;align-items:center;justify-content:center;font-size:11px;font-weight:700}
.cta-a{background:var(--white);color:var(--primary)}
.cta-b{border:1.5px solid var(--white);color:var(--white)}

/* footer */
.site-footer{top:4933px;height:372px;background:var(--footer);color:var(--white)}
.f-brand{left:144px;top:82px;display:flex;align-items:center;gap:10px;font-size:30px;font-weight:500}
.f-brand i{width:22px;height:22px;border-radius:50%;background:var(--white);display:block}
.f-note{left:144px;top:130px;width:290px;font-size:11px;line-height:18px;color:#dfe6f1}
.f-input{left:144px;top:183px;width:262px;height:30px;background:var(--white);border-radius:16px;display:flex;align-items:center;padding:0 6px 0 12px;gap:8px;font-size:10px;color:var(--muted)}
.f-input .go{margin-left:auto;width:22px;height:22px;border-radius:50%;border:1.5px solid var(--primary);display:flex;align-items:center;justify-content:center}
.f-col h4{font-size:15px;font-weight:500;margin-bottom:14px}
.f-col a{display:block;font-size:11.5px;color:#e4e9f1;text-decoration:none;line-height:28px}
.f-contact div{display:flex;gap:10px;font-size:11.5px;line-height:18px;color:#e4e9f1;margin-bottom:14px}
.f-social div{display:flex;align-items:center;gap:10px;font-size:11.5px;color:#e4e9f1;height:41px}
.f-social i{width:28px;height:28px;border-radius:50%;border:1.5px solid var(--white);display:flex;align-items:center;justify-content:center}
.f-social i b{width:8px;height:8px;background:var(--white);border-radius:50%}
.f-copy{top:331px;font-size:11px;color:#e4e9f1}
</style>
</head>
<body>

<header class="site-header">
  <div class="abs brand"><span class="brand-dot"></span>Tidal Ledger</div>
  <nav>
    <span class="abs nav-link" style="left:500px">Features</span>
    <span class="abs nav-link" style="left:591px">Industries</span>
    <span class="abs nav-link" style="left:689px">Pricing</span>
    <span class="abs nav-link" style="left:768px">Testimonials</span>
    <span class="abs nav-link" style="left:884px">Contact</span>
  </nav>
  <a class="abs btn btn-solid header-cta">Book a Demo</a>
</header>

<section class="hero">
  <h1 class="abs hero-title cond">Workforce Scheduling,<br>Magically Simple.</h1>
  <svg class="abs hero-curve" width="120" height="14" viewBox="0 0 120 14"><path d="M2 11 Q60 1 118 7" fill="none" stroke="#0054AA" stroke-width="2.5" stroke-linecap="round"/></svg>
  <p class="abs hero-text">Tidal Ledger automates roster creation across any industry — fair, intelligent, and built for operational efficiency.</p>
  <a class="abs btn btn-solid hero-btn1">Start Free Trial <svg width="12" height="10" viewBox="0 0 12 10"><path d="M1 5h9M6 1l4 4-4 4" stroke="#fff" stroke-width="1.6" fill="none"/></svg></a>
  <a class="abs btn btn-outline hero-btn2"><svg width="16" height="16" viewBox="0 0 16 16"><circle cx="8" cy="8" r="7" fill="none" stroke="#0054AA" stroke-width="1.3"/><path d="M6.5 5v6l4.5-3z" fill="#0054AA"/></svg>Book a Demo</a>
  <div class="abs hero-art" role="img" aria-label="Illustration of a person marking shifts on a large wall calendar"></div>
</section>

<section class="trust">
  <p class="abs center trust-label">TRUSTED BY FORWARD-THINKING TEAMS</p>
  <div class="abs trust-row">
    <span><i class="trust-sq"></i>Forgeworks</span>
    <span>Orbital</span>
    <span>Partnerly</span>
    <span>Brandmark</span>
    <span><i class="trust-sq"></i>Hexline</span>
  </div>
</section>

<section class="why">
  <p class="abs center eyebrow" style="top:70px">WHY TIDAL LEDGER</p>
  <h2 class="abs center sec-title cond" style="top:96px">Built for Modern Operations</h2>
  <div class="abs why-card" style="left:140px">
    <svg width="58" height="58" viewBox="0 0 58 58" fill="none" stroke="#0054AA" stroke-width="2"><path d="M29 6l18 7v14c0 12-8 20-18 25-10-5-18-13-18-25V13z"/><path d="M21 29l6 6 11-12"/></svg>
    <h3>Built-in Compliance</h3>
    <p>Automatically enforce award rates, rest periods, maximum hours, and industry-specific regulations.</p>
  </div>
  <div class="abs why-card" style="left:457px">
    <svg width="58" height="58" viewBox="0 0 58 58" fill="none" stroke="#0054AA" stroke-width="2"><circle cx="29" cy="29" r="10"/><circle cx="29" cy="29" r="20" stroke-dasharray="7 5"/><circle cx="29" cy="29" r="3" fill="#0054AA"/></svg>
    <h3>Intelligent Automation</h3>
    <p>AI builds your roster in seconds, factoring in availability, skills, and compliance rules automatically.</p>
  </div>
  <div class="abs why-card" style="left:776px">
    <svg width="58" height="58" viewBox="0 0 58 58" fill="none" stroke="#0054AA" stroke-width="2"><circle cx="18" cy="20" r="5"/><circle cx="40" cy="20" r="5"/><path d="M8 48V36c0-5 4-8 10-8s10 3 10 8v12M30 48V36c0-5 4-8 10-8s10 3 10 8v12M4 50h50"/></svg>
    <h3>Happier Teams</h3>
    <p>Fair shift distribution, self-service swaps, and transparent scheduling keep your staff engaged.</p>
  </div>
</section>

<section class="features">
  <p class="abs center eyebrow" style="top:70px">FEATURES</p>
  <h2 class="abs center sec-title cond" style="top:96px">Everything You Need to Run Smarter</h2>

  <div class="abs hex-wrap" style="left:186px;top:190px"><div class="hex active">
    <svg width="62" height="58" viewBox="0 0 62 58" fill="none" stroke="#fff" stroke-width="2"><rect x="6" y="8" width="50" height="44" rx="3"/><path d="M6 18h50M18 4v8M44 4v8"/><path d="M14 26h6v6h-6zM28 26h6v6h-6zM42 26h6v6h-6zM14 38h6v6h-6zM28 38h6v6h-6z"/></svg>
    <h3>Automated Scheduling</h3>
    <p>AI drafts rosters based on demand, skills &amp; preferences. 90% less manual drag.</p>
  </div></div>
  <div class="abs hex-wrap" style="left:468px;top:190px"><div class="hex">
    <svg width="62" height="62" viewBox="0 0 62 62" fill="none" stroke="#0054AA" stroke-width="2"><circle cx="31" cy="31" r="26"/><path d="M31 13l13 5v10c0 9-6 15-13 18-7-3-13-9-13-18V18z"/><path d="M25 30l5 5 8-9"/></svg>
    <h3>Compliance Engine</h3>
    <p>Real-time alerts for break rules, certifications, and local regulations.</p>
  </div></div>
  <div class="abs hex-wrap" style="left:750px;top:190px"><div class="hex">
    <svg width="62" height="62" viewBox="0 0 62 62" fill="none" stroke="#0054AA" stroke-width="2"><circle cx="28" cy="34" r="16"/><path d="M28 26v16M32 29c-2-2-8-2-8 1s8 2 8 6-6 3-8 1"/><circle cx="46" cy="16" r="8" stroke-dasharray="4 3"/></svg>
    <h3>Cost optimisation</h3>
    <p>Track wage % against sales, minimise overtime, shift cost insights.</p>
  </div></div>
  <div class="abs hex-wrap" style="left:328px;top:433px"><div class="hex">
    <svg width="62" height="62" viewBox="0 0 62 62" fill="none" stroke="#0054AA" stroke-width="2"><rect x="6" y="8" width="50" height="34" rx="3"/><path d="M24 50h14M31 42v8"/><circle cx="22" cy="25" r="6"/><path d="M34 22h14M34 28h10"/></svg>
    <h3>Multisite Support</h3>
    <p>Centralised or decentralized — unified view of 10+ locations.</p>
  </div></div>
  <div class="abs hex-wrap" style="left:610px;top:433px"><div class="hex">
    <svg width="62" height="62" viewBox="0 0 62 62" fill="none" stroke="#0054AA" stroke-width="2"><circle cx="18" cy="22" r="5"/><path d="M10 52V36c0-5 3-8 8-8s8 3 8 8v16"/><rect x="32" y="34" width="22" height="16" rx="2"/><circle cx="46" cy="14" r="7" stroke-dasharray="4 3"/></svg>
    <h3>Staff Self-service</h3>
    <p>Pick up open shifts, time-off requests, and team messaging.</p>
  </div></div>
</section>

<section class="industries">
  <p class="abs center eyebrow" style="top:76px">WHY TIDAL LEDGER</p>
  <h2 class="abs center sec-title cond" style="top:102px">Built for Modern Operations</h2>
  <div class="abs ind" style="left:198px"><div class="ind-circle active"><svg width="36" height="36" viewBox="0 0 36 36" fill="none" stroke="#fff" stroke-width="2"><path d="M18 3l12 5v9c0 8-5 13-12 16-7-3-12-8-12-16V8z"/><path d="M18 12v10M13 17h10"/></svg></div>Healthcare</div>
  <div class="abs ind" style="left:331px"><div class="ind-circle"><svg width="36" height="36" viewBox="0 0 36 36" fill="none" stroke="#0054AA" stroke-width="2"><path d="M5 14l3-8h20l3 8zM7 14v16h22V14M14 30v-9h8v9"/></svg></div>Retail</div>
  <div class="abs ind" style="left:465px"><div class="ind-circle"><svg width="36" height="36" viewBox="0 0 36 36" fill="none" stroke="#0054AA" stroke-width="2"><path d="M6 24a12 12 0 0 1 24 0zM4 24h28M18 9v3M4 30h28"/></svg></div>Hospitality</div>
  <div class="abs ind" style="left:599px"><div class="ind-circle"><svg width="36" height="36" viewBox="0 0 36 36" fill="none" stroke="#0054AA" stroke-width="2"><rect x="3" y="11" width="18" height="14"/><path d="M21 15h7l5 5v5H21z"/><circle cx="10" cy="27" r="3"/><circle cx="27" cy="27" r="3"/></svg></div>Logistics</div>
  <div class="abs ind" style="left:733px"><div class="ind-circle"><svg width="36" height="36" viewBox="0 0 36 36" fill="none" stroke="#0054AA" stroke-width="2"><circle cx="18" cy="10" r="6"/><path d="M3 31V21h9v10M14 31V21h9v10M25 31V21h8v10M2 31h32"/></svg></div>Manufacturing</div>
  <div class="abs ind" style="left:866px"><div class="ind-circle"><svg width="36" height="36" viewBox="0 0 36 36" fill="none" stroke="#0054AA" stroke-width="2"><path d="M18 4l11 4v8c0 7-5 12-11 14-6-2-11-7-11-14V8z"/><path d="M13 17l4 4 6-7"/></svg></div>Security</div>
  <div class="abs ind" style="left:1002px"><div class="ind-circle"><svg width="36" height="36" viewBox="0 0 36 36" fill="none" stroke="#0054AA" stroke-width="2"><rect x="5" y="7" width="26" height="24" rx="2"/><path d="M5 14h26M12 4v6M24 4v6M18 17l2 4 4 .5-3 3 1 4-4-2-4 2 1-4-3-3 4-.5z"/></svg></div>Events</div>
</section>

<section class="testimonials">
  <div class="abs center" style="top:73px;text-align:center"><span class="pill">TESTIMONIALS</span></div>
  <h2 class="abs center sec-title-alt" style="top:110px">Loved By Operations <b>Teams</b></h2>

  <div class="abs arrow" style="left:86px;background:#1d2a3d"><svg width="14" height="10" viewBox="0 0 14 10"><path d="M13 5H2M6 1L2 5l4 4" stroke="#fff" stroke-width="1.6" fill="none"/></svg></div>
  <div class="abs arrow" style="left:1076px;background:var(--primary)"><svg width="14" height="10" viewBox="0 0 14 10"><path d="M1 5h11M8 1l4 4-4 4" stroke="#fff" stroke-width="1.6" fill="none"/></svg></div>

  <div class="abs t-card" style="left:142px">
    <div class="t-avatar" role="img" aria-label="Portrait photo of the reviewer"></div>
    <div class="t-name">Milo Hartmann</div><div class="t-stars">★★★★★</div><div class="t-quote">99</div>
    <p class="t-text">Lorem Ipsum Is Simply Dummy Text Of The Printing And Typesetting Industry. Lorem Ipsum Has Been The Industry's Standard Dummy Text Ever Since The 1500s, When An Unknown Printer Took A Galley Of Type And Scrambled It To Make A Type Specimen Book.</p>
  </div>
  <div class="abs t-card" style="left:457px">
    <div class="t-avatar" style="background:linear-gradient(135deg,#e2c2a4,#b5a08d)" role="img" aria-label="Portrait photo of the reviewer"></div>
    <div class="t-name">Clara Voss</div><div class="t-stars">★★★★★</div><div class="t-quote">99</div>
    <p class="t-text">Lorem Ipsum Is Simply Dummy Text Of The Printing And Typesetting Industry. Lorem Ipsum Has Been The Industry's Standard Dummy Text Ever Since The 1500s, When An Unknown Printer Took A Galley Of Type And Scrambled It To Make A Type Specimen Book.</p>
  </div>
  <div class="abs t-card" style="left:770px">
    <div class="t-avatar" style="background:linear-gradient(135deg,#c99a78,#8f7667)" role="img" aria-label="Portrait photo of the reviewer"></div>
    <div class="t-name">Nora Lindqvist</div><div class="t-stars">★★★★★</div><div class="t-quote">99</div>
    <p class="t-text">Lorem Ipsum Is Simply Dummy Text Of The Printing And Typesetting Industry. Lorem Ipsum Has Been The Industry's Standard Dummy Text Ever Since The 1500s, When An Unknown Printer Took A Galley Of Type And Scrambled It To Make A Type Specimen Book.</p>
  </div>
</section>

<section class="pricing">
  <div class="abs center" style="top:93px;text-align:center"><span class="pill">PRICING</span></div>
  <h2 class="abs center sec-title-alt" style="top:130px">Simple, Transparent <b>Pricing</b></h2>
  <p class="abs center" style="top:192px;font-size:11px;text-align:center;color:#2c3545">Start Free, Scale As You Grow. No Hidden Fees.</p>

  <div class="abs p-card" style="left:142px">
    <svg width="66" height="58" viewBox="0 0 66 58" fill="none" stroke="#0054AA" stroke-width="2.4"><rect x="6" y="6" width="54" height="36" rx="3"/><path d="M24 52h18M33 42v10"/><path d="M14 34l10-10 8 6 14-14"/></svg>
    <h3>Starter</h3><p class="p-sub">Perfect for small teams getting started</p>
    <div class="p-price">$29<small>/ user / month</small></div>
    <div class="p-rule"></div><p class="p-get">What you will get</p>
    <ul class="p-list">
      <li><i class="tick"></i>Up to 25 employees</li><li><i class="tick"></i>Automated scheduling</li><li><i class="tick"></i>Staff self-service app</li><li><i class="tick"></i>Email notifications</li><li><i class="tick"></i>Basic reporting</li><li><i class="tick"></i>Priority support</li>
    </ul>
    <div class="p-btn">START FREE TRIAL</div>
  </div>
  <div class="abs p-card featured" style="left:453px">
    <span class="badge">MOST POPULAR</span>
    <svg width="66" height="58" viewBox="0 0 66 58" fill="none" stroke="#fff" stroke-width="2.4"><path d="M20 40c4-18 18-30 36-34-2 18-14 32-32 38z"/><circle cx="40" cy="22" r="5"/><path d="M20 40l-8 8M14 32l-6 2M28 46l-2 6"/></svg>
    <h3>Professional</h3><p class="p-sub">For growing teams that need more power</p>
    <div class="p-price">$99<small>/ user / month</small></div>
    <div class="p-rule"></div><p class="p-get">What you will get</p>
    <ul class="p-list">
      <li><i class="tick"></i>Up to 200 employees</li><li><i class="tick"></i>Everything in Starter</li><li><i class="tick"></i>Compliance engine</li><li><i class="tick"></i>Cost optimisation</li><li><i class="tick"></i>Multi-site dashboard</li><li><i class="tick"></i>Advanced analytics</li>
    </ul>
    <div class="p-btn">START FREE TRIAL</div>
  </div>
  <div class="abs p-card" style="left:764px">
    <svg width="66" height="58" viewBox="0 0 66 58" fill="none" stroke="#0054AA" stroke-width="2.4"><rect x="6" y="4" width="32" height="44" rx="2"/><path d="M12 14l3 3 5-6M12 26l3 3 5-6M12 38l3 3 5-6"/><circle cx="46" cy="40" r="12"/><path d="M46 33v14M49 36c-1-2-6-2-6 1s6 2 6 5-5 3-6 1"/></svg>
    <h3>Enterprise</h3><p class="p-sub">For large organisations with complex needs</p>
    <div class="p-choose">Choose Starter</div>
    <div class="p-rule"></div><p class="p-get">What you will get</p>
    <ul class="p-list">
      <li><i class="tick"></i>Unlimited employees</li><li><i class="tick"></i>Everything in Professional</li><li><i class="tick"></i>Custom integrations</li><li><i class="tick"></i>Dedicated account manager</li><li><i class="tick"></i>SLA &amp; uptime guarantee</li><li><i class="tick"></i>On-premise option</li>
    </ul>
    <div class="p-btn">CONTACT SALES</div>
  </div>
</section>

<section class="contact">
  <div class="abs center" style="top:94px;text-align:center"><span class="pill">GET IN TOUCH</span></div>
  <h2 class="abs center sec-title-alt" style="top:132px">Let's Build Your <b>Perfect Roster</b></h2>
  <p class="abs center contact-sub" style="text-align:center">Whether You're Scheduling 10 Staff Or 10,000 — We'd Love To Show You How Tidal Ledger<br>Can Simplify Your Operations.</p>
  <div class="abs field" style="left:292px;top:233px;width:301px"><svg width="14" height="14" viewBox="0 0 14 14" fill="none" stroke="#9aa3b0"><circle cx="7" cy="4.5" r="3"/><path d="M1.5 13c0-3 2.5-5 5.5-5s5.5 2 5.5 5"/></svg>Full Name</div>
  <div class="abs field" style="left:607px;top:233px;width:301px"><svg width="14" height="14" viewBox="0 0 14 14" fill="none" stroke="#9aa3b0"><circle cx="7" cy="4.5" r="3"/><path d="M1.5 13c0-3 2.5-5 5.5-5s5.5 2 5.5 5"/></svg>Company</div>
  <div class="abs field" style="left:292px;top:302px;width:301px"><svg width="14" height="14" viewBox="0 0 14 14" fill="none" stroke="#9aa3b0"><rect x="1" y="3" width="12" height="9"/><path d="M1 3l6 5 6-5"/></svg>Email</div>
  <div class="abs field" style="left:607px;top:302px;width:301px"><svg width="16" height="16" viewBox="0 0 16 16" fill="none" stroke="#9aa3b0"><rect x="2" y="2" width="12" height="13"/><path d="M5 5h2M9 5h2M5 8h2M9 8h2M7 15v-3h2v3"/></svg>Staff size<svg style="margin-left:auto" width="14" height="8" viewBox="0 0 14 8"><path d="M1 1l6 6 6-6" stroke="#3b4556" stroke-width="1.5" fill="none"/></svg></div>
  <div class="abs field" style="left:292px;top:370px;width:616px;height:103px;align-items:flex-start;padding-top:16px"><svg width="14" height="14" viewBox="0 0 14 14" fill="none" stroke="#9aa3b0"><circle cx="7" cy="7" r="6"/><path d="M4 6h6M4 8.5h4"/></svg>Message</div>
  <div class="abs contact-btn">BOOK A DEMO</div>
</section>

<section class="cta">
  <h2>Ready To Transform<br><b>Your Workforce?</b></h2>
  <p>Join Thousands Of Teams Who've Already Switched To Smarter, Fairer, Automated Scheduling.</p>
  <div class="cta-btns"><span class="cta-a">START FREE TRIAL</span><span class="cta-b">BOOK A DEMO</span></div>
</section>

<footer class="site-footer">
  <div class="abs f-brand"><i></i>Tidal Ledger</div>
  <p class="abs f-note">Latest Updates, Exclusive Content, And Special Offers? Subscribe To Our Newsletter!</p>
  <div class="abs f-input"><svg width="12" height="10" viewBox="0 0 12 10" fill="none" stroke="#6b7585"><rect x=".5" y=".5" width="11" height="9"/><path d="M.5 .5l5.5 5 5.5-5"/></svg>Your Email<span class="go"><svg width="10" height="8" viewBox="0 0 10 8"><path d="M1 4h8M6 1l3 3-3 3" stroke="#0054AA" stroke-width="1.4" fill="none"/></svg></span></div>

  <div class="abs f-col" style="left:510px;top:74px"><h4>Quick Links</h4><a>Home</a><a>Features</a><a>Industries</a><a>Pricing</a><a>Contact Us</a></div>
  <div class="abs f-col f-contact" style="left:686px;top:76px;width:210px"><h4>Contact Details</h4>
    <div><svg width="12" height="16" viewBox="0 0 12 16"><path d="M6 1a5 5 0 0 1 5 5c0 4-5 9-5 9S1 10 1 6a5 5 0 0 1 5-5z" fill="#fff"/><circle cx="6" cy="6" r="2" fill="#0d1a33"/></svg><span>77 Harbour Lane<br>Eastbank, QL 40210</span></div>
    <div><svg width="12" height="14" viewBox="0 0 14 14"><path d="M3 1l3 3-2 2c1 2 2 3 4 4l2-2 3 3-2 2C6 13 1 8 1 3z" fill="#fff"/></svg><span>Phone<br>+00 1 5550 0199</span></div>
    <div><svg width="12" height="12" viewBox="0 0 12 12" fill="none" stroke="#fff"><rect x=".5" y="2" width="11" height="8"/><path d="M.5 2l5.5 4 5.5-4"/></svg><span>Email<br>hello@tidalledger.example</span></div>
  </div>
  <div class="abs f-col f-social" style="left:949px;top:74px"><h4>Social Media</h4>
    <div><i><b></b></i>Community</div><div><i><b></b></i>Videos</div><div><i><b></b></i>Network</div><div><i><b></b></i>Gallery</div>
  </div>
  <p class="abs center f-copy" style="text-align:center">2025 Tidal Ledger. All Rights Reserved.</p>
</footer>

</body>
</html>
```